Web Design for Real Estate Lending business

I need a web design for my real estate private lending business. The name of the business is Halvern Capital Group. I plan on using Wordpress because that platform is the most optimized for SEO, and we will rely heavily on SEO after the website is built.

I want the website to be responsive of course, and have a fresh, professional, and sleek UI.

The 4 main goals of the website will be:
1. Rank in Google for our relevant key words (Los Angeles real estate hard money lending, real estate financing, fix and flip, private lending, etc)
2. Educate them on what our lending platform is capable of.
3. Capture the contact info (email or phone number) of investors & borrowers who are interested
4. Encourage investors and borrowers to contact us directly

This is an example of a similar business's website: https://www.morvelcapital.example/

Here is my business parter's old website:
https://web.archive.org/web/20180822043430/http://www.dumaleqg.example/

All of the information on that website (2nd link) will apply to our business. You can pull the information from that Dumale QG website and make it look more modern / sleek, similar to the 1st link (but better).

We are not selling anything on the website.

I also attached a business card template. I would like something similar to this but one that looks slightly more corporate / professional. Keep the colors the same though.

```html
<!DOCTYPE html>
<html lang="en">
<head>
<meta charset="utf-8">
<title>Halvern Capital Group – Hard Money Lending</title>
<link href="https://fonts.googleapis.com/css2?family=Poppins:wght@300;400;500;600;700&display=swap" rel="stylesheet">
<style>
:root{
  --blue:#2b6cb8;
  --blue-dark:#1f5ba6;
  --blue-light:#8fb6e2;
  --field:#dde7f3;
  --ink:#2a2a2a;
  --muted:#5a5a5a;
  --grey-bg:#f3f3f3;
  --black:#0d0d0d;
  --slate:#5b6673;
  --white:#fff;
}
*{box-sizing:border-box;margin:0;padding:0}
html,body{width:1200px;height:3677px;overflow:hidden}
body{font-family:'Poppins',sans-serif;color:var(--ink);background:var(--white);position:relative}
.abs{position:absolute}
a{color:inherit;text-decoration:none}

.topbar{left:0;top:0;width:1200px;height:27px;background:var(--black);color:var(--white);font-size:12px;display:flex;align-items:center;justify-content:center;gap:10px}
.header{left:0;top:27px;width:1200px;height:81px;background:var(--white)}
.brand{display:flex;align-items:center;gap:8px;color:var(--blue-dark);font-weight:700;line-height:1}
.brand-mark{width:34px;height:34px;background:var(--blue);flex:none}
.brand-name{font-size:24px;letter-spacing:.3px}
.brand-name small{display:block;font-size:16px;font-weight:700}
.header .brand{left:160px;top:16px}
.phone{left:654px;top:24px;display:flex;align-items:center;gap:10px;font-size:15px;color:var(--muted)}
.phone-ic{width:30px;height:30px;border:1.5px solid var(--blue);border-radius:50%;display:flex;align-items:center;justify-content:center}
.btn-outline,.btn-solid{display:flex;align-items:center;justify-content:center;font-size:13px;font-weight:500;text-transform:uppercase}
.btn-outline{border:1.5px solid var(--blue);color:var(--blue);background:var(--white)}
.btn-solid{background:var(--blue);color:var(--white)}
.nav{left:0;top:108px;width:1200px;height:38px;background:var(--blue);color:var(--white);font-size:12.5px;text-transform:uppercase}
.nav span{position:absolute;top:11px}

.hero{left:0;top:146px;width:1200px;height:459px;background:linear-gradient(90deg,#3e4247 0%,#6d7176 30%,#c9cbcc 55%,#e9e7e3 100%)}
.hero h1{left:160px;top:66px;font-size:54px;line-height:64px;font-weight:600;color:var(--white);letter-spacing:1px}
.hero ul{left:160px;top:203px;list-style:none;color:var(--white);font-size:18px;font-weight:500}
.hero li{display:flex;align-items:center;gap:16px;height:35px}
.hex-dot{width:15px;height:15px}
.hero .btn-solid{left:166px;top:348px;width:162px;height:35px;font-size:13.5px}

.about{left:0;top:605px;width:1200px;height:508px;text-align:center}
.about-title{left:0;top:92px;width:1200px;display:flex;justify-content:center;align-items:center;gap:22px}
.about-title h2{font-size:36px;font-weight:600;color:var(--blue-dark)}
.about-title .brand-name{font-size:21px}
.about-title .brand-name small{font-size:14px}
.about-title .brand-mark{width:34px;height:34px}
.about h3{left:0;top:153px;width:1200px;font-size:17px;font-weight:500;color:var(--ink)}
.about p{left:230px;top:183px;width:740px;font-size:13.5px;line-height:25px;color:var(--muted)}
.about .btn-outline{left:517px;top:312px;width:165px;height:37px;font-size:13px}
.badges{left:180px;top:382px;width:840px;height:43px;display:flex;align-items:center;justify-content:space-between}
.badge{width:120px;height:30px;background:#d6d6d6;border-radius:4px}
.badge-sep{width:1px;height:34px;background:#cfcfcf}

.services{left:0;top:1113px;width:1200px;height:634px;background:var(--grey-bg)}
.services h2{left:0;top:68px;width:1200px;text-align:center;font-size:36px;font-weight:600;color:var(--blue-dark)}
.services .lead{left:0;top:132px;width:1200px;text-align:center;font-size:17px;color:var(--ink)}
.diagram{left:0;top:0;width:1200px;height:634px}
.svc-label{font-size:15.5px;color:var(--blue);font-weight:500;white-space:nowrap}
.svc-label.l{text-align:right}

.features{left:0;top:1747px;width:1200px;height:622px}
.feature{width:270px;text-align:center}
.hex-photo{width:220px;height:250px;margin:0 auto;clip-path:polygon(50% 0,100% 25%,100% 75%,50% 100%,0 75%,0 25%)}
.feature h4{margin-top:52px;font-size:14.5px;font-weight:500;color:var(--blue);text-transform:uppercase}
.feature p{margin-top:8px;font-size:12.5px;line-height:20.5px;color:var(--muted)}
.feature a{display:inline-block;margin-top:6px;font-size:12.5px;color:#8a9bb0;text-decoration:underline}

.cta{left:0;top:2369px;width:1200px;height:371px;background:linear-gradient(90deg,#5a8fcf 0%,#4a80c4 45%,#3f74b8 100%);color:var(--white);text-align:center}
.cta h2{left:0;top:76px;width:1200px;font-size:34px;font-weight:600;letter-spacing:1px}
.cta p{left:240px;top:140px;width:720px;font-size:20px;line-height:26px;font-weight:300}
.cta .btn-cta{left:545px;top:254px;width:110px;height:37px;background:var(--white);color:var(--blue);font-size:13px;font-weight:500;display:flex;align-items:center;justify-content:center}

.deco{position:absolute}
.form-sec{left:0;top:2740px;width:1200px;height:624px}
.form-sec h2{left:0;top:85px;width:1200px;text-align:center;font-size:36px;font-weight:600;color:var(--blue-dark)}
.form-sec .lead{left:0;top:132px;width:1200px;text-align:center;font-size:14px;font-weight:500}
.field{background:var(--field);display:flex;align-items:flex-start;font-size:14px;color:var(--muted)}
.field .ic{width:42px;height:100%;border-right:1px solid #b9c6d6;display:flex;align-items:flex-start;justify-content:center;padding-top:14px;flex:none}
.field .ph{padding:12px 0 0 11px}
.question{left:0;top:414px;width:1200px;text-align:center;font-size:13.5px;color:var(--muted)}
.checks{left:0;top:449px;width:1200px;display:flex;justify-content:center;gap:18px;font-size:13px;color:var(--muted)}
.checks label{display:flex;align-items:center;gap:7px}
.box{width:13px;height:13px;border:1px solid #b8c3d1;background:var(--white);display:flex;align-items:center;justify-content:center}
.box.on::after{content:"";width:7px;height:7px;background:var(--blue)}
.form-sec .btn-solid{left:551px;top:496px;width:97px;height:38px;font-size:13px}

.footer{left:0;top:3364px;width:1200px;height:269px;background:var(--grey-bg)}
.footer h5{font-size:15.5px;font-weight:500;color:var(--ink);text-transform:uppercase;letter-spacing:.3px}
.flinks{font-size:13px;color:var(--muted);line-height:28.5px}
.contact-item{display:flex;gap:10px;font-size:13px;color:var(--muted);line-height:18px}
.contact-item b{font-weight:400;color:var(--ink);display:block}
.footer .brand{left:786px;top:75px}
.footer .brand-mark{width:48px;height:48px}
.footer .brand-name{font-size:31px}
.footer .brand-name small{font-size:22px}
.footer .about-co{left:786px;top:154px;width:260px;font-size:12.5px;line-height:18px;color:var(--muted)}
.follow{left:786px;top:220px;display:flex;align-items:center;gap:7px;font-size:13px;color:var(--ink)}
.soc{width:26px;height:26px;border-radius:50%}
.bottombar{left:0;top:3633px;width:1200px;height:44px;background:var(--black);color:#d8d8d8;font-size:13.5px;display:flex;align-items:center;justify-content:center}
.bottombar b{font-weight:500;color:var(--white);margin:0 4px}
</style>
</head>
<body>

<div class="abs topbar">
  <span>Los Angeles Real Estate Hard Money Lending</span><span>|</span>
  <span>Real Estate Financing</span><span>|</span>
  <span>Fix And Flip</span><span>|</span>
  <span>Private Lending</span>
</div>

<header class="abs header">
  <a class="abs brand" href="#"><span class="brand-mark"></span><span class="brand-name">HALVERN<small>CAPITAL GROUP</small></span></a>
  <div class="abs phone">
    <span class="phone-ic"><svg width="14" height="14" viewBox="0 0 24 24"><path fill="#2b6cb8" d="M6.6 10.8a15.1 15.1 0 0 0 6.6 6.6l2.2-2.2c.3-.3.7-.4 1-.2 1.1.4 2.3.6 3.6.6.6 0 1 .4 1 1V20c0 .6-.4 1-1 1A17 17 0 0 1 3 4c0-.6.4-1 1-1h3.5c.6 0 1 .4 1 1 0 1.3.2 2.5.6 3.6.1.3 0 .7-.2 1z"/></svg></span>
    +1 (555) 013-2207
  </div>
  <a class="abs btn-outline" href="#" style="left:833px;top:21px;width:89px;height:36px">Investor</a>
  <a class="abs btn-solid" href="#" style="left:935px;top:21px;width:104px;height:36px">Borrower</a>
</header>

<nav class="abs nav">
  <span style="left:163px">Loan Options</span>
  <span style="left:300px">Property Values</span>
  <span style="left:455px">Property Types</span>
  <span style="left:601px">Investors</span>
  <span style="left:714px">Recommended Professionals</span>
  <span style="left:955px">Contact Us</span>
</nav>

<section class="abs hero" role="img" aria-label="Photo of a smiling family carrying moving boxes into a bright new home">
  <h1 class="abs">HARD MONEY<br>LENDING</h1>
  <ul class="abs">
    <li><svg class="hex-dot" viewBox="0 0 20 20"><polygon points="10,1 18,5.5 18,14.5 10,19 2,14.5 2,5.5" fill="none" stroke="#fff" stroke-width="4"/></svg>No Hassle Process</li>
    <li><svg class="hex-dot" viewBox="0 0 20 20"><polygon points="10,1 18,5.5 18,14.5 10,19 2,14.5 2,5.5" fill="none" stroke="#fff" stroke-width="4"/></svg>Quick Qualify</li>
    <li><svg class="hex-dot" viewBox="0 0 20 20"><polygon points="10,1 18,5.5 18,14.5 10,19 2,14.5 2,5.5" fill="none" stroke="#fff" stroke-width="4"/></svg>We Work With All Credit</li>
    <li><svg class="hex-dot" viewBox="0 0 20 20"><polygon points="10,1 18,5.5 18,14.5 10,19 2,14.5 2,5.5" fill="none" stroke="#fff" stroke-width="4"/></svg>We'll Get You What You Need</li>
  </ul>
  <a class="abs btn-solid" href="#">Contact Us Today</a>
</section>

<section class="abs about">
  <div class="abs about-title">
    <h2>ABOUT</h2>
    <span class="brand"><span class="brand-mark"></span><span class="brand-name">HALVERN<small>CAPITAL GROUP</small></span></span>
  </div>
  <h3 class="abs">Your Fast and Reliable Hard Money Specialists</h3>
  <p class="abs">Do you need hard money in hurry to purchase investment property,build your dream home or quick cash?<br>When banks say no, Halvern Capital Group says YES!<br>Welcome to Halvern Capital Group. With more than 100 years combined experience our trained professionals have the good knowledge and expertise to customize a loan specific to your needs. We are a private lender.</p>
  <a class="abs btn-outline" href="#">Contact Us Today</a>
  <div class="abs badges">
    <span class="badge"></span><span class="badge-sep"></span>
    <span class="badge"></span><span class="badge-sep"></span>
    <span class="badge"></span><span class="badge-sep"></span>
    <span class="badge"></span><span class="badge-sep"></span>
    <span class="badge"></span>
  </div>
</section>

<section class="abs services">
  <h2 class="abs">OUR SERVICES</h2>
  <p class="abs lead">Some Types of Real Estate/Property to serve as Collateral Include</p>
  <svg class="abs diagram" viewBox="0 0 1200 634">
    <defs>
      <g id="node">
        <circle r="37" fill="none" stroke="#8fb6e2" stroke-width="2" stroke-dasharray="5 4"/>
        <circle r="29" fill="#fff" stroke="#8fb6e2" stroke-width="5"/>
        <rect x="-10" y="-12" width="20" height="22" fill="none" stroke="#2b6cb8" stroke-width="1.6"/>
        <path d="M-5 -7h3M2 -7h3M-5 -2h3M2 -2h3M-5 3h3M2 3h3" stroke="#2b6cb8" stroke-width="1.6"/>
      </g>
    </defs>
    <g stroke="#9aa7b6" stroke-width="1" stroke-dasharray="4 3">
      <line x1="600" y1="371" x2="528" y2="227"/><line x1="600" y1="371" x2="467" y2="300"/>
      <line x1="600" y1="371" x2="420" y2="375"/><line x1="600" y1="371" x2="467" y2="447"/>
      <line x1="600" y1="371" x2="528" y2="521"/><line x1="600" y1="371" x2="671" y2="227"/>
      <line x1="600" y1="371" x2="736" y2="300"/><line x1="600" y1="371" x2="781" y2="375"/>
      <line x1="600" y1="371" x2="736" y2="447"/><line x1="600" y1="371" x2="671" y2="521"/>
    </g>
    <polygon points="567,293 633,293 679,339 679,405 633,451 567,451 521,405 521,339" fill="#5b6673"/>
    <polygon points="571,303 629,303 669,343 669,401 629,441 571,441 531,401 531,343" fill="#fff"/>
    <rect x="580" y="352" width="40" height="40" fill="#2b6cb8"/>
    <use href="#node" x="528" y="227"/><use href="#node" x="467" y="300"/>
    <use href="#node" x="420" y="375"/><use href="#node" x="467" y="447"/>
    <use href="#node" x="528" y="521"/><use href="#node" x="671" y="227"/>
    <use href="#node" x="736" y="300"/><use href="#node" x="781" y="375"/>
    <use href="#node" x="736" y="447"/><use href="#node" x="671" y="521"/>
  </svg>
  <span class="abs svc-label l" style="right:728px;top:217px">Hospitality Properties</span>
  <span class="abs svc-label l" style="right:789px;top:290px">Industrial Properties</span>
  <span class="abs svc-label l" style="right:836px;top:365px">Self Storages</span>
  <span class="abs svc-label l" style="right:789px;top:437px">Retail Centers</span>
  <span class="abs svc-label l" style="right:728px;top:510px">Mobile Home Parks</span>
  <span class="abs svc-label" style="left:726px;top:217px">Multi-Family Apartments</span>
  <span class="abs svc-label" style="left:792px;top:290px">Mobile Home Parks</span>
  <span class="abs svc-label" style="left:835px;top:365px">Condo Units</span>
  <span class="abs svc-label" style="left:791px;top:437px">Office Buildings</span>
  <span class="abs svc-label" style="left:726px;top:510px">Assisted Living Condos</span>
</section>

<section class="abs features">
  <article class="abs feature" style="left:168px;top:94px">
    <div class="hex-photo" role="img" aria-label="Photo of a stressed man at a desk holding up a stack of bills" style="background:linear-gradient(135deg,#e9edf2,#9fb4cf 60%,#6f85a3)"></div>
    <h4>Bills Piling Up?</h4>
    <p>With Halvern Capital Group, you'll be back on top of your mountain of paperwork instead of buried underneath it! Let the experienced team members here help consolidate your debt.</p>
    <a href="#">Debt Consolidation</a> ›
  </article>
  <article class="abs feature" style="left:465px;top:94px">
    <div class="hex-photo" role="img" aria-label="Photo of a contractor in a hard hat reviewing building plans with a client" style="background:linear-gradient(135deg,#c6ccd3,#8b95a1 55%,#c96a3b)"></div>
    <h4>Finance Your Project</h4>
    <p>Building a new property? Expanding an operation? Not sure what kind of funding you need? Halvern Capital Group will help you get the funds you need to get the project done!</p>
    <a href="#">Ask A Private Lender</a> ›
  </article>
  <article class="abs feature" style="left:761px;top:94px">
    <div class="hex-photo" role="img" aria-label="Photo of two businessmen shaking hands" style="background:linear-gradient(135deg,#f2f4f7,#b9c3cf 55%,#44505e)"></div>
    <h4>Recommended Professionals</h4>
    <p>These are individuals and companies that Halvern Capital Group works with and trust to provide you with the same level of service you have come to expect here over the years.</p>
    <a href="#">See Who Is Recommended!</a> ›
  </article>
</section>

<section class="abs cta" role="img" aria-label="Blue-tinted photo of two businessmen talking across a desk in an office">
  <h2 class="abs">GET CASH NOW!</h2>
  <p class="abs">Get FREE advice from one of the experienced professionals here regarding any Private Money Loan related topics. It's quick, it's easy, and/or the more questions you answer + the more accurate your results.</p>
  <a class="abs btn-cta" href="#">GET STARTED</a>
</section>

<section class="abs form-sec">
  <span class="deco" style="left:103px;top:24px;width:37px;height:90px;background:var(--blue)"></span>
  <span class="deco" style="left:174px;top:24px;width:37px;height:76px;background:var(--slate)"></span>
  <span class="deco" style="left:244px;top:24px;width:36px;height:36px;background:var(--blue-light)"></span>
  <h2 class="abs">STAY INFORMED</h2>
  <p class="abs lead">Lorem ipsum dolor sit amet consectetuer adipiscing elit</p>

  <div class="abs field" style="left:260px;top:177px;width:331px;height:44px">
    <span class="ic"><svg width="13" height="13" viewBox="0 0 24 24"><path fill="#444" d="M22 2 2 11l8 3 3 8z"/></svg></span><span class="ph">Email*</span>
  </div>
  <div class="abs field" style="left:609px;top:177px;width:330px;height:44px">
    <span class="ic"><svg width="12" height="13" viewBox="0 0 24 24"><circle cx="12" cy="7" r="5" fill="#444"/><path fill="#444" d="M3 22c0-6 4-9 9-9s9 3 9 9z"/></svg></span><span class="ph">Name*</span>
  </div>
  <div class="abs field" style="left:260px;top:237px;width:331px;height:44px">
    <span class="ic"><svg width="11" height="13" viewBox="0 0 20 24"><rect x="2" y="1" width="16" height="22" fill="#444"/><rect x="6" y="5" width="3" height="3" fill="#dde7f3"/><rect x="11" y="5" width="3" height="3" fill="#dde7f3"/><rect x="6" y="11" width="3" height="3" fill="#dde7f3"/><rect x="11" y="11" width="3" height="3" fill="#dde7f3"/></svg></span><span class="ph">Company*</span>
  </div>
  <div class="abs field" style="left:609px;top:237px;width:330px;height:44px">
    <span class="ic"><svg width="13" height="12" viewBox="0 0 24 20"><rect x="1" y="5" width="22" height="14" rx="2" fill="#444"/><rect x="8" y="1" width="8" height="5" fill="none" stroke="#444" stroke-width="2"/></svg></span><span class="ph">Job Title</span>
  </div>
  <div class="abs field" style="left:260px;top:297px;width:679px;height:81px">
    <span class="ic"><svg width="13" height="13" viewBox="0 0 24 24"><rect x="2" y="4" width="17" height="17" fill="none" stroke="#444" stroke-width="2"/><path d="M9 15l1-4L20 1l3 3-10 10z" fill="#444"/></svg></span><span class="ph">Message*</span>
  </div>

  <p class="abs question">What information are you most interested in? (Select all that apply)</p>
  <div class="abs checks">
    <label><span class="box on"></span>Investor Newsletter</label>
    <label><span class="box"></span>Borrower Newsletter</label>
  </div>
  <a class="abs btn-solid" href="#">Submit</a>
</section>

<footer class="abs footer">
  <h5 class="abs" style="left:163px;top:72px">Quick Links</h5>
  <div class="abs flinks" style="left:163px;top:98px">Home<br>About<br>Glossary<br>Checklists<br>Property Values</div>
  <div class="abs flinks" style="left:280px;top:98px">Property Types<br>Local Resources<br>Recommended Professionals<br>Privacy Policy<br>Terms of Use</div>

  <h5 class="abs" style="left:512px;top:72px">Contact Details</h5>
  <div class="abs contact-item" style="left:512px;top:102px">
    <svg width="10" height="14" viewBox="0 0 20 28"><path fill="#2b6cb8" d="M10 0a10 10 0 0 0-10 10c0 7 10 18 10 18s10-11 10-18A10 10 0 0 0 10 0zm0 14a4 4 0 1 1 0-8 4 4 0 0 1 0 8z"/></svg>
    <span>418 Harbor Crest Dr<br>Bayview Beach, CA. 90000</span>
  </div>
  <div class="abs contact-item" style="left:512px;top:147px">
    <svg width="12" height="12" viewBox="0 0 24 24"><path fill="#2b6cb8" d="M6.6 10.8a15.1 15.1 0 0 0 6.6 6.6l2.2-2.2c.3-.3.7-.4 1-.2 1.1.4 2.3.6 3.6.6.6 0 1 .4 1 1V20c0 .6-.4 1-1 1A17 17 0 0 1 3 4c0-.6.4-1 1-1h3.5c.6 0 1 .4 1 1 0 1.3.2 2.5.6 3.6.1.3 0 .7-.2 1z"/></svg>
    <span><b>Call Us</b>(555) 013-2207</span>
  </div>
  <div class="abs contact-item" style="left:506px;top:197px">
    <svg width="14" height="14" viewBox="0 0 24 24"><path fill="#2b6cb8" d="M22 2 2 11l8 3 3 8z"/></svg>
    <span><b>Mail Us</b>info@halvern.example</span>
  </div>

  <div class="abs brand"><span class="brand-mark"></span><span class="brand-name">HALVERN<small>CAPITAL GROUP</small></span></div>
  <p class="abs about-co">Lorem ipsum dolor sit ame consectetuer adipiscing elit sed diam. Lorem ipsum dolor sit ame consectetuer...</p>
  <div class="abs follow">Folllow Us
    <span class="soc" style="background:#3b6fd1;margin-left:6px"></span>
    <span class="soc" style="background:#5aa3e8"></span>
    <span class="soc" style="background:#5b6673"></span>
  </div>
</footer>

<div class="abs bottombar">Copyright © 2021 <b>Halvern Capital Group.</b> All Rights Reserved.</div>

</body>
</html>
```